Business cards for Paperleaf Sprites

Please note that the color of the logo has been changed from green to teal blue. Sorry for the changing!

Anything will go but want to have some funky side.

I would like the front of the business card is the logo and business information and the back side is the Adult Coloring, so that would attract the customer to do the coloring on the other side. Have more interactive side. (pictures for references only can see it below). Fairies on the back of the card for coloring and whatever you want to adds on to color, like flowers, nature etc......

Scrapbooking is not just paper, it also involves watercolor, mixed media, art, all the fun stuff.

Another keypoint I would like to stress on is the back of the business card should be Adult Coloring and make sure you are not google and use the search engine to copy and paste because of the copyright issue.

As a designer, I am sure you all can create beautiful artwork.

Please submit your creativities!

Want the business card is out of the ordinary and customers would like to keep that as a keepsake rather than treat like a regular business card and trash it. Fonts cannot be too small, consider some of the customers have to wear bi-focal eyeglasses.

Thanks a lot!

Target Market(s)

Scrapbooking, Card making, papercraft, stampin‘ , gifts items , etc.

Industry/Entity Type

Retail

Contact Information for Business Card

Color Scheme, please match with the Logo. Watercolor effect is nice!
Thanks!

Font styles to use
Serif

Requirements
Must have
• I would like Elegant and playful.
• Thanks!
Nice to have
• Watercolor effect or check out the Adult Coloring Book, I am thinking we can use a double-sided business card, one side for the information and the other side for people can do the coloring. I have attached 2 pictures for reference.
Should not have
• No black color on the background please!

```html
<!DOCTYPE html>
<html lang="en">
<head>
<meta charset="utf-8">
<title>Paperleaf Sprites – Business Card</title>
<link rel="stylesheet" href="https://fonts.googleapis.com/css2?family=Bitter:wght@400;500;600;700&display=swap">
<style>
  :root {
    --page-bg: #d8d0c5;
    --card-bg: #efe8de;
    --card-edge: #f7f2ea;
    --teal: #2e7777;
    --red: #b13a2e;
    --ink: #4a4038;
    --leaf-warm: #dc8e62;
    --leaf-rose: #d9a08c;
    --leaf-dusk: #a89280;
  }
  * { margin: 0; padding: 0; box-sizing: border-box; }
  html, body {
    width: 1200px; height: 1047px; overflow: hidden;
    background: var(--page-bg);
    font-family: "Bitter", Georgia, serif;
  }
  .card {
    position: absolute; left: 151px; top: 291px;
    width: 946px; height: 515px;
    background: var(--card-bg);
    border: 2px solid var(--card-edge);
    border-radius: 20px;
    overflow: hidden;
  }
  .leaf-scatter {
    position: absolute; left: 5px; top: 0;
    width: 324px; height: 164px;
    background: linear-gradient(135deg, var(--leaf-warm) 0%, var(--leaf-rose) 50%, var(--leaf-dusk) 100%);
    opacity: .6;
    clip-path: polygon(0 0, 72% 0, 100% 58%, 86% 78%, 40% 100%, 0 100%);
  }
  .brand {
    position: absolute; left: 22px; top: 184px;
    width: 464px; height: 210px;
    display: flex; align-items: center; justify-content: center;
  }
  .brand-name {
    color: var(--teal);
    font-weight: 600; font-size: 44px; letter-spacing: 1px;
    white-space: nowrap;
  }
  .divider {
    position: absolute; left: 514px; top: 151px;
    width: 3px; height: 279px;
    background: var(--teal);
  }
  .details { position: absolute; left: 542px; top: 143px; }
  .person-name {
    font-size: 42px; font-weight: 600; line-height: 46px; letter-spacing: .5px;
    white-space: nowrap;
  }
  .person-name .first { color: var(--teal); }
  .person-name .last { color: var(--red); }
  .person-role {
    margin-top: 9px;
    font-size: 22px; line-height: 28px; font-weight: 600; color: var(--ink); letter-spacing: .3px;
  }
  .contact-list { list-style: none; margin-top: 34px; }
  .contact-list li {
    display: flex; align-items: flex-start;
    font-size: 20px; font-weight: 500; color: var(--ink);
    line-height: 34px; letter-spacing: .4px; white-space: nowrap;
  }
  .contact-list svg {
    flex: none; width: 18px; height: 18px;
    margin: 8px 18px 0 0; fill: var(--teal);
  }
</style>
</head>
<body>
  <div class="card">
    <div class="leaf-scatter" role="img" aria-label="Scattered autumn leaves decoration"></div>

    <div class="brand">
      <span class="brand-name">Paperleaf Sprites</span>
    </div>

    <div class="divider"></div>

    <div class="details">
      <h1 class="person-name"><span class="first">MARA</span> <span class="last">ELLISON</span></h1>
      <p class="person-role">PRESIDENT/OWNER</p>
      <ul class="contact-list">
        <li>
          <svg viewBox="0 0 24 24" aria-hidden="true"><path d="M6.6 10.8a15 15 0 0 0 6.6 6.6l2.2-2.2a1 1 0 0 1 1-.25 11.4 11.4 0 0 0 3.6.57 1 1 0 0 1 1 1V20a1 1 0 0 1-1 1A17 17 0 0 1 3 4a1 1 0 0 1 1-1h3.5a1 1 0 0 1 1 1c0 1.25.2 2.45.57 3.57a1 1 0 0 1-.25 1z"/></svg>
          <span>+12-555-01470</span>
        </li>
        <li>
          <svg viewBox="0 0 24 24" aria-hidden="true"><path d="M2 5h20v14H2z M4 7v.5l8 5 8-5V7l-8 5z" fill-rule="evenodd"/></svg>
          <span>maraellison@paperleaf.com</span>
        </li>
        <li>
          <svg viewBox="0 0 24 24" aria-hidden="true"><path d="M12 2a10 10 0 1 0 0 20 10 10 0 0 0 0-20zm7.9 9h-3.4a15 15 0 0 0-1.3-5.6A8 8 0 0 1 19.9 11zM12 4.1c.9 1.2 2.3 3.6 2.5 6.9h-5C9.7 7.7 11.1 5.3 12 4.1zM8.8 5.4A15 15 0 0 0 7.5 11H4.1a8 8 0 0 1 4.7-5.6zM4.1 13h3.4a15 15 0 0 0 1.3 5.6A8 8 0 0 1 4.1 13zm7.9 6.9c-.9-1.2-2.3-3.6-2.5-6.9h5c-.2 3.3-1.6 5.7-2.5 6.9zm3.2-1.3a15 15 0 0 0 1.3-5.6h3.4a8 8 0 0 1-4.7 5.6z"/></svg>
          <span>www.paperleafsprites.com</span>
        </li>
        <li>
          <svg viewBox="0 0 24 24" aria-hidden="true"><path d="M12 2a7 7 0 0 0-7 7c0 5.2 7 13 7 13s7-7.8 7-13a7 7 0 0 0-7-7zm0 9.5A2.5 2.5 0 1 1 12 6.5a2.5 2.5 0 0 1 0 5z"/></svg>
          <span>Willow Crest Lane Fernvale<br>OR 97001,USA</span>
        </li>
      </ul>
    </div>
  </div>
</body>
</html>
```